Cover for Where the Quiet River Bends Beyond Our Morning

Cover for a book that describes everything that happens to a person, from pre-birth life plans through growing in compassion and wisdom to death and living in the afterlife. The information is revealed in messages from people living in the life after this life. The title is Lanterns Along the Hidden Stair of Every Soul: Gathered from Voices Dwelling in the Further Meadow. Author is T. Morven Ashdale. Book size is 6 by 9.

Target Market(s)

General

Font styles to use
Serif

```html
<!DOCTYPE html>
<html lang="en">
<head>
<meta charset="utf-8">
<title>Lanterns Along the Hidden Stair of Every Soul — Cover</title>
<link href="https://fonts.googleapis.com/css2?family=Cormorant+Garamond:wght@400;500;600&family=EB+Garamond:wght@400&display=swap" rel="stylesheet">
<style>
  :root {
    --page-bg: #eeeeee;
    --paper: #ffffff;
    --ink: #1a1a1a;
    --teal: #17607f;
    --teal-pale: #d9e8ee;
    --rule: #2f6f8a;
  }
  * { box-sizing: border-box; margin: 0; padding: 0; }
  html, body { width: 899px; height: 1200px; overflow: hidden; }
  body {
    background: var(--page-bg);
    position: relative;
    font-family: "EB Garamond", Georgia, serif;
    color: var(--ink);
  }
  .cover-spread {
    position: absolute;
    left: 14px; top: 300px;
    width: 871px; height: 601px;
    background: var(--paper);
    box-shadow: 0 2px 8px rgba(0,0,0,0.18);
  }
  /* Back cover */
  .back-cover { position: absolute; left: 0; top: 0; width: 422px; height: 100%; }
  .back-emblem { position: absolute; left: 165px; top: 81px; width: 66px; height: 51px; }
  .back-blurb {
    position: absolute; left: 37px; top: 168px; width: 337px;
    font-size: 8.7px; line-height: 11px; text-align: justify; hyphens: auto;
  }
  .back-blurb p + p { margin-top: 11px; }

  /* Spine */
  .spine { position: absolute; left: 422px; top: 0; width: 32px; height: 100%; }
  .spine-title {
    position: absolute; left: 50%; top: 35px;
    transform: translateX(-50%);
    writing-mode: vertical-rl;
    font-family: "EB Garamond", Georgia, serif;
    font-size: 13.5px; white-space: nowrap;
  }
  .spine-emblem { position: absolute; left: 5px; top: 440px; width: 22px; height: 18px; }
  .spine-author {
    position: absolute; left: 50%; top: 476px;
    transform: translateX(-50%);
    writing-mode: vertical-rl;
    font-family: "Cormorant Garamond", Georgia, serif;
    font-size: 7.5px; letter-spacing: 0.3em; white-space: nowrap;
  }

  /* Front cover */
  .front-cover { position: absolute; left: 454px; top: 0; width: 417px; height: 100%; text-align: center; }
  .front-tagline {
    position: absolute; left: 0; right: 0; top: 44px;
    font-family: "Cormorant Garamond", Georgia, serif;
    font-weight: 600; font-size: 11.5px; line-height: 16px;
    letter-spacing: 0.16em; text-transform: uppercase;
  }
  .front-emblem { position: absolute; left: 82px; top: 108px; width: 254px; height: 191px; }
  .title-rule { position: absolute; left: 158px; width: 110px; height: 1px; background: var(--rule); }
  .title-rule--top { top: 329px; }
  .title-rule--bottom { top: 493px; }
  .front-title {
    position: absolute; left: 0; right: 0; top: 350px;
    font-family: "Cormorant Garamond", Georgia, serif;
    font-weight: 500; font-size: 29px; line-height: 36px;
  }
  .front-author {
    position: absolute; left: 0; right: 0; top: 535px;
    font-family: "Cormorant Garamond", Georgia, serif;
    font-weight: 500; font-size: 16px; letter-spacing: 0.3em; text-transform: uppercase;
  }
</style>
</head>
<body>
<svg width="0" height="0" style="position:absolute">
  <defs>
    <linearGradient id="wing-fade" x1="0" y1="0" x2="0" y2="1">
      <stop offset="0" stop-color="#17607f"/>
      <stop offset="0.45" stop-color="#5f93aa"/>
      <stop offset="1" stop-color="#e4eef2"/>
    </linearGradient>
  </defs>
</svg>

<main class="cover-spread">
  <section class="back-cover">
    <svg class="back-emblem" viewBox="0 0 66 51" role="img" aria-label="Small teal butterfly illustration">
      <rect width="66" height="51" rx="10" fill="url(#wing-fade)"/>
    </svg>
    <div class="back-blurb">
      <p>Lorem ipsum dolor sit amet, consectetur adipiscing elit. Maecenas aliquet aliquam leo nec pellentesque. Nam imperdiet dignissim est, in lacinia purus varius vitae. Aliquam nec tellus eget risus blandit aliquam vel nec mi. Morbi dignissim ex blandit justo efficitur gravida. Morbi vitae justo scelerisque, placerat velit nec, ornare urna. Mauris eget nunc pellentesque, vehicula ligula non, elementum nibh. Ut at porttitor magna, finibus porttitor lorem. Quisque vitae mi ac diam venenatis dapibus sed id sapien. Quisque varius, turpis sit amet tempor faucibus, magna lorem pulvinar felis, non fermentum neque tellus ut velit. Vivamus quis aliquet turpis, a auctor nunc. Proin cursus et orci eget commodo. Nam placerat sem in nisi dapibus porttitor. Nulla auctor varius leo, commodo porta eros dapibus elementum. Nullam cursus enim ac mi efficitur, vel egestas elit ultrices. Pellentesque elit augue, semper in quam at, tristique accumsan massa. Proin efficitur gravida turpis eu placerat.</p>
      <p>Nunc eros dui, dapibus sit amet eros sed, consectetur ullamcorper ipsum. Fusce auctor, ipsum non congue ullamcorper, tellus odio semper lectus, id elementum dui nibh quis lacus. Curabitur pharetra dolor id nisi bibendum aliquam. Aliquam vestibulum porta elit id varius. Aenean est mi, posuere vel nibh nec, varius malesuada eros. Ut fringilla nulla vitae mi venenatis, et suscipit tellus egestas. Curabitur in mi finibus, euismod urna ac, iaculis odio.</p>
    </div>
  </section>

  <section class="spine">
    <div class="spine-title">Lanterns Along the Hidden Stair of Every Soul</div>
    <svg class="spine-emblem" viewBox="0 0 22 18" role="img" aria-label="Tiny teal butterfly illustration">
      <rect width="22" height="18" rx="4" fill="url(#wing-fade)"/>
    </svg>
    <div class="spine-author">T. Morven Ashdale</div>
  </section>

  <section class="front-cover">
    <p class="front-tagline">Gathered from voices dwelling<br>in the Further Meadow</p>
    <svg class="front-emblem" viewBox="0 0 254 191" role="img" aria-label="Large butterfly illustration fading from deep teal wingtips to white">
      <rect width="254" height="191" rx="30" fill="url(#wing-fade)"/>
    </svg>
    <div class="title-rule title-rule--top"></div>
    <h1 class="front-title">Lanterns Along<br>the Hidden Stair<br>of Every Soul</h1>
    <div class="title-rule title-rule--bottom"></div>
    <p class="front-author">T. Morven Ashdale</p>
  </section>
</main>
</body>
</html>
```